New York IT Service, Technology & Security Co.

need a new business card design for our Technology & Security Company. We are a Computer Networking Company, Security Camera Installers, Phone Systems.

Target Market(s)

Construction, Medical, Law Offices, Accounting, Retail etc.

Industry/Entity Type

Information Technology

Logo is attached, colors are Blue, Red, Black. Blue for Technology & Red is for Security Cameras, Access Control, Alarm Systems

Colors
fbed22
ec1f27
0555a3
ffffff

Requirements
Must have
• Pictures or Icons for
• For Technology:
• Computer, Network, Phone System, Copier, TV, Cabling
• For Security:
• Video Surveillance, Access Control, Intercom, Fire Alarm, Burglar Alarm, Time Clock

```html
<!DOCTYPE html>
<html lang="en">
<head>
<meta charset="utf-8">
<title>Bayline Tech Works – Business Card</title>
<link href="https://fonts.googleapis.com/css2?family=Roboto:wght@400;500;700;900&family=Roboto+Condensed:wght@500;700&display=swap" rel="stylesheet">
<style>
  :root {
    --blue: #0a6fb8;
    --blue-dark: #0555a3;
    --red: #e20a17;
    --ink: #1b1b1b;
    --grey: #4a4a4a;
    --white: #ffffff;
    --paper: #f4f4f4;
    --backdrop: #e7e2da;
  }
  * { margin: 0; padding: 0; box-sizing: border-box; }
  html, body { width: 1200px; height: 960px; overflow: hidden; }
  body {
    position: relative;
    background: var(--backdrop);
    font-family: "Roboto", Arial, sans-serif;
  }

  .card {
    position: absolute;
    width: 600px;
    height: 338px;
    box-shadow: 0 3px 8px rgba(0,0,0,0.25);
  }

  /* Front face */
  .card-front {
    left: 322px; top: 106px;
    background: var(--blue);
    color: var(--white);
    text-align: center;
  }
  .card-front .brand {
    position: absolute; left: 0; right: 0; top: 84px;
    font-weight: 900; font-size: 30px; letter-spacing: 0.5px;
    color: var(--white);
  }
  .services { position: absolute; left: 0; right: 0; top: 164px; }
  .service-group + .service-group { margin-top: 14px; }
  .service-heading {
    font-weight: 700; font-size: 14.5px; margin-bottom: 3px;
  }
  .service-heading.security { color: var(--red); font-weight: 500; }
  .service-line { font-size: 14.5px; line-height: 18px; }
  .dot {
    display: inline-block; width: 5px; height: 5px; border-radius: 50%;
    background: var(--white); vertical-align: middle; margin: 0 3px;
  }
  .dot.red { background: var(--red); }

  /* Back face */
  .card-back {
    left: 320px; top: 493px;
    background: var(--paper);
  }
  .card-back .brand {
    position: absolute; left: 0; width: 332px; top: 132px;
    text-align: center;
    font-weight: 900; font-size: 22px; color: var(--ink);
  }
  .divider {
    position: absolute; left: 332px; top: 56px; width: 2px; height: 186px;
    background: linear-gradient(to bottom, transparent, #b9b9b9 20%, #b9b9b9 80%, transparent);
  }
  .contact { position: absolute; left: 363px; top: 56px; color: var(--grey); }
  .person-name {
    font-family: "Roboto Condensed", Arial, sans-serif;
    font-weight: 700; font-size: 24px; color: var(--blue); line-height: 28px;
  }
  .person-title {
    font-family: "Roboto Condensed", Arial, sans-serif;
    font-weight: 500; font-size: 16px; color: var(--red); line-height: 18px;
  }
  .address { font-size: 14.5px; line-height: 18px; margin-top: 13px; }
  .contact-list { list-style: none; margin-top: 9px; }
  .contact-list li {
    display: flex; align-items: center; font-size: 14.5px; line-height: 19px;
  }
  .contact-list svg { width: 14px; height: 14px; margin-right: 9px; fill: var(--blue); }

  .web-band {
    position: absolute; left: 0; right: 0; top: 280px; height: 37px;
    display: flex;
  }
  .web-band .band-blue {
    flex: 0 0 430px; background: var(--blue);
    display: flex; align-items: center; padding-left: 73px;
    color: var(--white); font-weight: 700; font-size: 14px; letter-spacing: 5.6px;
  }
  .web-band .band-red { flex: 1; background: var(--red); }
</style>
</head>
<body>

  <section class="card card-front" aria-label="Card front">
    <div class="brand">BAYLINE TECH WORKS</div>
    <div class="services">
      <div class="service-group">
        <p class="service-heading">FOR TECHNOLOGY</p>
        <p class="service-line">Computer<span class="dot"></span>Network<span class="dot"></span>Phone System</p>
        <p class="service-line">Copier<span class="dot"></span>TV <span class="dot"></span> Cabling</p>
      </div>
      <div class="service-group">
        <p class="service-heading security">FOR SECURITY</p>
        <p class="service-line">Video Surveillance<span class="dot red"></span>Access Control<span class="dot red"></span>Intercom</p>
        <p class="service-line">Fire Alarm<span class="dot red"></span>Burglar Alarm<span class="dot red"></span>Time Clock</p>
      </div>
    </div>
  </section>

  <section class="card card-back" aria-label="Card back">
    <div class="brand">BAYLINE TECH WORKS</div>
    <div class="divider"></div>
    <div class="contact">
      <p class="person-name">DANIEL REYES</p>
      <p class="person-title">CEO/FOUNDER</p>
      <p class="address">2140 Cedar Hollow Road<br>Fairbanks, Alaska 34612</p>
      <ul class="contact-list">
        <li>
          <svg viewBox="0 0 16 16" aria-hidden="true"><path d="M3.6 1.2l2.3 2.6-1.3 1.9c.9 2 2.5 3.6 4.5 4.5l1.9-1.3 2.6 2.3-1.4 2.3C6.9 15.3.7 9.1 1.3 2.6z"/></svg>
          555 014 2291
        </li>
        <li>
          <svg viewBox="0 0 16 16" aria-hidden="true"><path d="M4 1h8v14H4zM5.5 2.5v9h5v-9zM7.2 12.6h1.6v1.2H7.2z" fill-rule="evenodd"/></svg>
          555 017 3846
        </li>
        <li>
          <svg viewBox="0 0 16 16" aria-hidden="true"><path d="M4 1h8v4H4zM1 6h14v6h-2v3H3v-3H1zM4.5 10v3.5h7V10z" fill-rule="evenodd"/></svg>
          555 019 5207
        </li>
        <li>
          <svg viewBox="0 0 16 16" aria-hidden="true"><path d="M1 3.5h14v9H1zM2.5 5v.4L8 9l5.5-3.6V5L8 8.5z" fill-rule="evenodd"/></svg>
          daniel@BaylineTech.com
        </li>
      </ul>
    </div>
    <div class="web-band">
      <div class="band-blue">www.BaylineTech.com</div>
      <div class="band-red"></div>
    </div>
  </section>

</body>
</html>
```